Flyer design for mental health and disability support work company.

The company name 'Harbourlight Disability'

we need a flyer design for our company.

Specialising
Harbourlight Disability is a new KWPS service aimed towards KWPS participants with psychosocial/mental health, intellectual, and cognitive disabilities. We also specialise in supporting participants with a history of being involved in the criminal justice system.

Our focus
Focusing on providing core KWPS supports for community participation, daily activities and supported independent living.

Authentic
Like-minded people passionate about wanting to make a difference in participants' lives.

Our aim is to provide holistic and empowering support targeted towards creating independence and guidance for all participants and families.

Over 35 years of experience working with people with a vast range of disabilities and individual support needs.

Extensive experience not only within KWPS but working with mainstream services within NSW Fairway, Health, Corrections and Parole, Housing, Civic Desk NSW, Welbridge, Brief Assist, QTOB and NSW court systems.

website www.harbourlightdisability.com.au
email for referrals send to - referrals@harbourlightdisability.com.au
for further information send to - hello@harbourlightdisability.com.au

number 1800 372 519

Font styles to use
Serif

Requirements
Should not have
• pictures with people that have disabilities

```html
<!DOCTYPE html>
<html lang="en">
<head>
<meta charset="utf-8">
<title>Harbourlight Disability – Flyer</title>
<link rel="stylesheet" href="https://fonts.googleapis.com/css2?family=Anton&family=Arimo:wght@400;700&family=Arvo:wght@700&family=Noto+Serif:wght@400;700&display=swap">
<style>
  :root{
    --backdrop:#0a5b7e;
    --navy:#163a5f;
    --sky:#86b3d3;
    --paper:#ffffff;
    --ink:#1b1b1b;
    --photo-light:#eef0f2;
    --photo-mid:#d9dde1;
    --skin:#e6c3b0;
    --skin-deep:#d6a58e;
  }
  *{margin:0;padding:0;box-sizing:border-box}
  html,body{width:1200px;height:2400px;overflow:hidden}
  body{background:var(--backdrop);position:relative;font-family:"Arimo",Arial,sans-serif}
  .flyer{position:absolute;left:50px;top:422px;width:1100px;height:1556px;background:var(--paper);overflow:hidden;box-shadow:0 20px 40px rgba(0,0,0,.35)}
  .flyer-shapes{position:absolute;inset:0;width:1100px;height:1556px}
  .hero-photo{position:absolute;left:0;top:300px;width:1100px;height:700px;
    background:
      radial-gradient(ellipse 420px 200px at 620px 330px, var(--skin) 0%, rgba(230,195,176,.6) 45%, rgba(230,195,176,0) 75%),
      radial-gradient(ellipse 260px 120px at 930px 160px, var(--skin-deep) 0%, rgba(214,165,142,0) 80%),
      radial-gradient(ellipse 240px 90px at 180px 320px, var(--skin) 0%, rgba(230,195,176,0) 80%),
      linear-gradient(180deg, rgba(255,255,255,0) 0%, var(--photo-mid) 30%, var(--photo-light) 70%, var(--paper) 100%);}
  .logo-badge{position:absolute;left:182px;top:86px;width:330px;height:330px;border-radius:50%;background:var(--navy);border:6px solid var(--sky);display:flex;flex-direction:column;align-items:center;justify-content:center}
  .logo-name{font-family:"Arvo",Georgia,serif;font-weight:700;font-size:30px;line-height:1.25;color:var(--paper);letter-spacing:1px;text-transform:uppercase}
  .title{position:absolute;left:586px;top:96px}
  .title-main{display:block;font-family:"Anton",Impact,sans-serif;font-size:80px;line-height:1;color:var(--navy);letter-spacing:1px}
  .title-sub{display:block;font-family:"Arimo",Arial,sans-serif;font-weight:700;font-size:80px;line-height:1.1;color:var(--sky)}
  .feature{position:absolute;width:440px}
  .feature-head{display:flex;align-items:center;gap:20px;margin-bottom:10px}
  .feature-head svg{width:44px;height:44px;flex:none}
  .feature-title{font-family:"Arvo",Georgia,serif;font-weight:700;font-size:40px;color:var(--navy);line-height:1}
  .feature p{font-size:22px;line-height:26.5px;color:var(--ink)}
  .feature p + p{margin-top:14px}
  .feature--specialising{left:116px;top:758px}
  .feature--focus{left:588px;top:758px}
  .feature--authentic{left:116px;top:955px}
  .feature--aim{left:588px;top:955px;width:450px}
  .services-band{position:absolute;left:138px;top:1226px;width:789px;height:36px;background:var(--navy);color:var(--paper);font-weight:700;font-size:21px;letter-spacing:.5px;display:flex;align-items:center;justify-content:center;white-space:nowrap}
  .contact{position:absolute;left:0;top:1312px;font-family:"Noto Serif",Georgia,serif;color:var(--paper)}
  .contact-title{margin-left:159px;font-weight:700;font-size:29px;text-decoration:underline;text-underline-offset:6px}
  .contact-row{display:flex;align-items:center;margin-left:64px;margin-top:10px}
  .contact-row svg{width:30px;height:30px;flex:none;margin-right:28px}
  .contact-row span{font-size:20px;line-height:24px}
  .contact-row--phone span{font-size:34px;font-weight:400;letter-spacing:1px}
</style>
</head>
<body>
<main class="flyer">
  <div class="hero-photo" role="img" aria-label="Photograph of a younger hand gently holding an older person's hand on a soft light background"></div>

  <svg class="flyer-shapes" viewBox="0 0 1100 1556" aria-hidden="true">
    <path d="M0 0H650Q150 60 0 440Z" fill="var(--sky)"/>
    <path d="M0 0H600Q130 40 0 370Z" fill="var(--navy)"/>
    <path d="M0 1268L472 1298L628 1525Q969 1483 1100 1088V1556H0Z" fill="var(--sky)"/>
    <path d="M0 1304H472L610 1531Q957 1507 1100 1112V1556H0Z" fill="var(--navy)"/>
  </svg>

  <div class="logo-badge">
    <span class="logo-name">Harbourlight</span>
    <span class="logo-name">Disability</span>
  </div>

  <h1 class="title">
    <span class="title-main">HARBOURLIGHT</span>
    <span class="title-sub">Disability</span>
  </h1>

  <section class="feature feature--specialising">
    <div class="feature-head">
      <svg viewBox="0 0 44 44"><g fill="var(--navy)"><circle cx="22" cy="22" r="14"/><g stroke="var(--navy)" stroke-width="7"><path d="M22 2v40M2 22h40M8 8l28 28M36 8L8 36"/></g></g><circle cx="22" cy="22" r="9" fill="#fff"/><path d="M22 16l2 4.5 4.5.4-3.4 3 1 4.5L22 26l-4.1 2.4 1-4.5-3.4-3 4.5-.4z" fill="var(--navy)"/></svg>
      <h2 class="feature-title">Specialising</h2>
    </div>
    <p>Harbourlight Disability is a new KWPS service aimed toward KWPS participants with a history of criminal justice, psychosocial/ mental health, intellectual, and cognitive disabilities.</p>
  </section>

  <section class="feature feature--focus">
    <div class="feature-head">
      <svg viewBox="0 0 44 44" fill="none" stroke="var(--navy)" stroke-width="2"><circle cx="22" cy="22" r="13"/><circle cx="22" cy="22" r="6"/><path d="M22 2v12M22 30v12M2 22h12M30 22h12"/></svg>
      <h2 class="feature-title">Our focus</h2>
    </div>
    <p>Focusing on providing core KWPS supports for community participation, daily activities and supported independent living.</p>
  </section>

  <section class="feature feature--authentic">
    <div class="feature-head">
      <svg viewBox="0 0 44 44" fill="none" stroke="var(--navy)" stroke-width="4"><path d="M36 22v16H6V8h24"/><path d="M12 20l9 9L40 6"/></svg>
      <h2 class="feature-title">Authentic</h2>
    </div>
    <p>Likeminded people wanting to make a difference in participant's lives.</p>
    <p>Experience in working with mainstream supports under, Justice, NSW Wellcare, Corrections,</p>
  </section>

  <section class="feature feature--aim">
    <div class="feature-head">
      <svg viewBox="0 0 44 44" fill="none" stroke="var(--navy)" stroke-width="2.5"><path d="M6 30A17 17 0 0 1 30 6M38 14A17 17 0 0 1 14 38" stroke-dasharray="4 3"/><circle cx="22" cy="22" r="9" stroke-width="5" stroke-dasharray="4 3"/><circle cx="22" cy="22" r="3" fill="var(--navy)"/></svg>
      <h2 class="feature-title">Our aim</h2>
    </div>
    <p>Our aim to provide holistic and empowering supports targeted towards creating indepen-dence and guidance for all participants and families.<br>Over 35 years of experience working with people that have psychosocial, intellectual, and cognitive disabilities.</p>
  </section>

  <div class="services-band">Housing, Civic Desk NSW, Welbridge, Brief Assist and Court processes.</div>

  <section class="contact">
    <h2 class="contact-title">Contact us :</h2>
    <div class="contact-row">
      <svg viewBox="0 0 30 30" fill="none" stroke="#fff" stroke-width="1.6"><circle cx="15" cy="15" r="13"/><path d="M15 23s-5-6-5-9.5a5 5 0 0 1 10 0C20 17 15 23 15 23z"/><circle cx="15" cy="13.5" r="1.8"/></svg>
      <span>111 Street Name, city name, State name,<br>country, 12345</span>
    </div>
    <div class="contact-row contact-row--phone">
      <svg viewBox="0 0 30 30" fill="none" stroke="#fff" stroke-width="1.6"><circle cx="15" cy="15" r="13"/><path d="M10 8l3 3-1.5 2.5c1 2 2.5 3.5 4.5 4.5L18.5 16.5l3 3-2 2C14 21 9 16 8.5 10z"/></svg>
      <span>123 456 789</span>
    </div>
    <div class="contact-row">
      <svg viewBox="0 0 30 30" fill="none" stroke="#fff" stroke-width="1.6"><circle cx="15" cy="15" r="13"/><rect x="8" y="10" width="14" height="10" fill="#fff"/><path d="M8 10l7 5 7-5" stroke="var(--navy)"/></svg>
      <span>harbourlightdisability.com</span>
    </div>
    <div class="contact-row">
      <svg viewBox="0 0 30 30" fill="none" stroke="#fff" stroke-width="1.4"><circle cx="15" cy="15" r="13"/><circle cx="15" cy="15" r="9"/><ellipse cx="15" cy="15" rx="4" ry="9"/><path d="M6 15h18M7.5 10.5h15M7.5 19.5h15"/></svg>
      <span>www.harbourlightdisability.com</span>
    </div>
  </section>
</main>
</body>
</html>
```